Landing Page One on One With Dr. Korvel

Hello!

I am looking for a high converting Landing Page for a One on One Coaching program that Dr. Korvel is releasing. I created a moch up for content but the spacing and graphics are not cohesive. I like the medical look at the top of the first page - the image is the graphic "Get One ON One Support from Dr. Korvel.
Please let me know if you have any questions!
Thank you!

```html
<!DOCTYPE html>
<html lang="en">
<head>
<meta charset="utf-8">
<title>Dr. Korvel – One on One Coaching</title>
<link href="https://fonts.googleapis.com/css2?family=Oswald:wght@400;500;600;700&family=Open+Sans:wght@400;600&display=swap" rel="stylesheet">
<style>
:root{
  --blue:#1d45a5;
  --blue-deep:#123a96;
  --orange:#e8891c;
  --ink:#222831;
  --grey:#8a8f98;
  --line:#e3e5ea;
  --soft:#f6f7f9;
  --white:#ffffff;
}
*{margin:0;padding:0;box-sizing:border-box}
html,body{width:1200px;height:3398px;overflow:hidden}
body{position:relative;background:var(--white);font-family:"Open Sans",Arial,sans-serif;color:var(--ink)}
.abs{position:absolute}
.oswald{font-family:"Oswald",Arial,sans-serif}

/* header */
.brand{left:141px;top:26px;font-family:"Oswald",sans-serif;font-weight:600;font-size:42px;color:var(--blue);display:flex;align-items:center;gap:10px;letter-spacing:.5px}
.brand-dot{width:22px;height:22px;border-radius:50%;background:var(--blue)}
.header-phone{left:758px;top:30px;display:flex;align-items:center;gap:10px;font-family:"Oswald",sans-serif;font-size:19px;color:var(--blue)}
.btn-head{left:918px;top:24px;width:148px;height:38px;background:var(--blue);color:var(--white);font-family:"Oswald",sans-serif;font-size:15px;display:flex;align-items:center;justify-content:center}

/* hero */
.hero{left:0;top:0;width:1200px;height:600px;background:linear-gradient(180deg,#f2f4f7 0%,#e8ecf1 70%,#eef1f4 100%);clip-path:polygon(0 0,100% 0,100% 530px,0 600px)}
.hero-doctor{left:682px;top:70px;width:388px;height:495px;background:linear-gradient(180deg,#c9ced6 0%,#e9ebef 55%,#f4f5f7 100%)}
.hero-title{left:170px;top:228px;font-family:"Oswald",sans-serif;font-weight:600;font-size:44px;color:var(--blue)}
.hero-sub{left:272px;top:296px;font-family:"Oswald",sans-serif;font-size:29px;color:var(--ink)}
.hero-tag{left:262px;top:350px;font-family:"Oswald",sans-serif;font-size:28px;color:var(--grey)}
.btn-read{left:292px;top:416px;width:106px;height:31px;border-radius:16px;background:var(--blue);color:var(--white);font-family:"Oswald",sans-serif;font-size:13px;display:flex;align-items:center;justify-content:center}

/* intro */
.intro-title{left:139px;top:654px;width:330px;font-family:"Oswald",sans-serif;font-weight:500;font-size:19px;line-height:36px;color:var(--ink)}
.intro-text{left:139px;top:742px;width:531px;font-size:11.5px;line-height:24px;color:var(--grey)}
.commit-title{left:139px;top:882px;font-family:"Oswald",sans-serif;font-weight:500;font-size:19px}
.goal{width:130px;text-align:center;font-family:"Oswald",sans-serif;font-size:12px;line-height:17px;color:var(--ink)}
.goal-icon{width:48px;height:48px;margin:0 auto 12px;border:2px solid var(--orange);border-radius:50%;display:flex;align-items:center;justify-content:center}

/* appointment card */
.appt{left:722px;top:650px;width:346px;height:571px;background:var(--white);border:1px solid var(--line);box-shadow:0 2px 10px rgba(0,0,0,.06)}
.appt-head{height:98px;background:var(--blue);color:var(--white);text-align:center;padding-top:14px;font-family:"Oswald",sans-serif}
.appt-head h2{font-size:25px;font-weight:500}
.appt-head p{font-size:18px;margin-top:4px}
.appt-or{position:absolute;left:157px;top:82px;width:32px;height:32px;border-radius:50%;background:var(--white);border:1px solid var(--line);font-size:10px;display:flex;align-items:center;justify-content:center;color:var(--ink)}
.field{position:absolute;left:28px;width:298px;height:47px;border:1px solid var(--line);font-size:11px;color:#aab0b8;padding:14px 12px}
.field.tall{height:85px}
.btn-book{position:absolute;left:28px;top:505px;width:298px;height:47px;background:var(--orange);color:var(--white);font-family:"Oswald",sans-serif;font-size:16px;display:flex;align-items:center;justify-content:center;letter-spacing:.5px}

/* pillars */
.pillars{left:0;top:1283px;width:1200px;height:595px;background:linear-gradient(180deg,var(--blue) 0%,var(--blue-deep) 100%);clip-path:polygon(0 60px,100% 0,100% 540px,0 595px)}
.pillars-title{left:0;top:1366px;width:1200px;text-align:center;font-family:"Oswald",sans-serif;font-size:19px;line-height:32px;color:var(--white);font-weight:500}
.pillars-title span{color:var(--orange)}
.pillar{width:330px;color:var(--white)}
.pillar h3{font-family:"Oswald",sans-serif;font-weight:500;font-size:18px;display:flex;align-items:center;gap:12px;margin-bottom:10px}
.pillar p{font-size:11.5px;line-height:22px}

/* video */
.video-title{left:0;top:1930px;width:1200px;text-align:center;font-family:"Oswald",sans-serif;font-weight:500;font-size:20px}
.video-title span{color:var(--orange)}
.video-sub{left:0;top:1966px;width:1200px;text-align:center;font-size:13px;color:var(--grey)}
.video{left:216px;top:2031px;width:765px;height:317px;background:linear-gradient(135deg,#3b4b63 0%,#6d5a45 50%,#2c3444 100%)}
.play{left:573px;top:2164px;width:50px;height:50px;border-radius:50%;border:3px solid var(--white);background:rgba(0,0,0,.35)}

/* signup */
.signup{left:0;top:2424px;width:1200px;height:160px;background:var(--blue)}
.signup-text{left:0;top:2462px;width:1200px;text-align:center;font-family:"Oswald",sans-serif;font-size:19px;color:var(--white);font-weight:500}
.signup-text span{color:var(--orange)}
.btn-sign{left:459px;top:2513px;width:181px;height:36px;border-radius:18px;background:var(--orange);color:var(--white);font-family:"Oswald",sans-serif;font-size:14px;display:flex;align-items:center;justify-content:center}

/* testimonials */
.testi{left:0;top:2584px;width:1200px;height:386px;background:var(--soft)}
.testi-title{left:0;top:2632px;width:1200px;text-align:center;font-family:"Oswald",sans-serif;font-weight:500;font-size:19px}
.card{top:2732px;width:243px;height:153px;border:1px solid #b9bdc4;border-radius:18px;background:var(--white);text-align:center;padding:42px 22px 0}
.card p{font-size:10.5px;line-height:18px;color:var(--grey)}
.card h4{margin-top:12px;font-size:12px;font-weight:600;color:var(--ink)}
.avatar{top:2697px;width:66px;height:66px;border-radius:50%;border:3px solid var(--white);background:linear-gradient(180deg,#9aa3ad,#6d7580)}
.arrow{top:2802px;font-size:18px;color:#b4b8bf}

/* footer */
.footer{left:0;top:2970px;width:1200px;height:428px;background:linear-gradient(180deg,var(--blue) 0%,var(--blue-deep) 100%)}
.foot-title{left:0;top:3022px;width:1200px;text-align:center;font-family:"Oswald",sans-serif;font-weight:500;font-size:26px;color:var(--white)}
.foot-sub{left:0;top:3070px;width:1200px;text-align:center;font-size:13px;color:var(--white)}
.btn-foot{left:461px;top:3115px;width:257px;height:50px;background:var(--orange);color:var(--white);font-family:"Oswald",sans-serif;font-size:19px;display:flex;align-items:center;justify-content:center}
.foot-call{left:0;top:3188px;width:1200px;text-align:center;font-family:"Oswald",sans-serif;font-size:20px;color:var(--white)}
.socials{left:447px;top:3247px;display:flex;gap:15px}
.social{width:37px;height:37px;background:rgba(255,255,255,.85);border-radius:3px}
.copy{left:0;top:3326px;width:1200px;text-align:center;font-size:11px;color:var(--white)}
</style>
</head>
<body>

<!-- hero -->
<div class="abs hero"></div>
<div class="abs hero-doctor" role="img" aria-label="Photo of Dr. Korvel in a white coat with arms crossed"></div>
<div class="abs brand"><span>DR. KORVEL</span><span class="brand-dot"></span></div>
<div class="abs header-phone">
  <svg width="20" height="20" viewBox="0 0 24 24"><circle cx="12" cy="12" r="11" fill="none" stroke="#1d45a5" stroke-width="1.6"/><path d="M8.5 7.5c.6-.6 1.2-.6 1.6 0l1 1.5c.3.5.2 1-.2 1.3l-.7.5c.5 1.2 1.5 2.2 2.7 2.7l.5-.7c.3-.4.8-.5 1.3-.2l1.5 1c.6.4.6 1 0 1.6-.9.9-2.3 1.1-3.6.4-2-1-3.6-2.6-4.6-4.6-.6-1.3-.4-2.6.5-3.5z" fill="#1d45a5"/></svg>
  <span>(800) 555 0142</span>
</div>
<div class="abs btn-head">Make Appointment</div>
<div class="abs hero-title">Get One on One Support</div>
<div class="abs hero-sub">from Dr.Korvel</div>
<div class="abs hero-tag">Total wellness Coaching Program</div>
<div class="abs btn-read">Read More</div>

<!-- intro -->
<div class="abs intro-title">CONCIERGE TOTAL WELLNESS FROM A PRACTICING MD!</div>
<p class="abs intro-text">Lorem ipsum dolor sit amet, consectetuer adipiscing elit. Aenean commodo ligula eget dolor. Aenean massa. Cum sociis natoque penatibus et magnis dis parturient montes, nascetur ridiculus mus. Donec quam felis, ultricies nec, pellentesque eu, pretium quis, sem. Nulla consequat massa quis enim. Donec pede justo, fringilla vel, aliquet nec, vulputate eget, arcu. Sed montes, nascetur ridiculus mus. Donec quam felis.Donec pede justo, fringilla vel, aliquet nec, vulputate eget, arcu.</p>
<div class="abs commit-title">MAKE A COMMITMENT YOURSELF</div>

<div class="abs goal" style="left:107px;top:948px"><div class="goal-icon"><svg width="22" height="22" viewBox="0 0 24 24" fill="none" stroke="#e8891c" stroke-width="2"><path d="M3 12h18M7 8v8M17 8v8"/></svg></div>Weight Loss</div>
<div class="abs goal" style="left:250px;top:948px"><div class="goal-icon"><svg width="22" height="22" viewBox="0 0 24 24" fill="none" stroke="#e8891c" stroke-width="2"><circle cx="12" cy="12" r="9"/><path d="M8 14c1 2 7 2 8 0"/><circle cx="9" cy="10" r=".8"/><circle cx="15" cy="10" r=".8"/></svg></div>Conquer Mental<br>illness</div>
<div class="abs goal" style="left:398px;top:948px"><div class="goal-icon"><svg width="22" height="22" viewBox="0 0 24 24" fill="#e8891c"><circle cx="6" cy="9" r="2.5"/><circle cx="12" cy="7" r="3"/><circle cx="18" cy="9" r="2.5"/><path d="M2 18c0-3 2-5 4-5s4 2 4 5zM8 18c0-4 2-6 4-6s4 2 4 6zM14 18c0-3 2-5 4-5s4 2 4 5z"/></svg></div>Build a Better<br>tribe</div>
<div class="abs goal" style="left:552px;top:948px"><div class="goal-icon"><svg width="22" height="22" viewBox="0 0 24 24" fill="#e8891c"><circle cx="12" cy="14" r="6"/><path d="M10 3h4v5h-4z"/></svg></div>Combat Stress<br>&amp; Disease</div>

<div class="abs goal" style="left:107px;top:1084px"><div class="goal-icon"><svg width="22" height="22" viewBox="0 0 24 24" fill="#e8891c"><path d="M13 2L5 14h6l-1 8 8-12h-6z"/></svg></div>Increase Energy</div>
<div class="abs goal" style="left:250px;top:1084px"><div class="goal-icon"><svg width="22" height="22" viewBox="0 0 24 24" fill="none" stroke="#e8891c" stroke-width="2"><circle cx="12" cy="5" r="2"/><path d="M12 8v6l-3 7M12 14l3 7M8 10h8"/></svg></div>Live<br>Joyfully</div>
<div class="abs goal" style="left:398px;top:1084px"><div class="goal-icon"><svg width="22" height="22" viewBox="0 0 24 24" fill="#e8891c"><path d="M12 21s-8-5-8-11a4.5 4.5 0 0 1 8-3 4.5 4.5 0 0 1 8 3c0 6-8 11-8 11z"/></svg></div>Cultivate<br>Relationships</div>
<div class="abs goal" style="left:552px;top:1084px"><div class="goal-icon"><svg width="22" height="22" viewBox="0 0 24 24" fill="none" stroke="#e8891c" stroke-width="2"><circle cx="12" cy="10" r="7"/><path d="M9 17v4h6v-4"/></svg></div>Clarify Your<br>Purpose</div>

<!-- appointment card -->
<div class="abs appt">
  <div class="appt-head"><h2>MAKE AN APPOINTMENT</h2><p>Call: (800) 555 0142</p></div>
  <div class="appt-or">OR</div>
  <div class="field" style="top:144px">Full Name</div>
  <div class="field" style="top:208px">Email Address</div>
  <div class="field" style="top:272px">Phone Number</div>
  <div class="field" style="top:336px">Date &amp; Time</div>
  <div class="field tall" style="top:403px">Additional Information</div>
  <div class="btn-book">BOOK AN APPOINTMENT</div>
</div>

<!-- pillars -->
<div class="abs pillars" role="img" aria-label="Blue-tinted photo of healthy food behind the five pillars"></div>
<div class="abs pillars-title">Dr.Korvel Coaches You One on One in areas based on his<br><span>Five Pilar Formula for Total Wellness</span></div>

<div class="abs pillar" style="left:150px;top:1488px"><h3><svg width="24" height="24" viewBox="0 0 24 24" fill="none" stroke="#fff" stroke-width="2"><circle cx="12" cy="12" r="6"/><path d="M3 4v16M21 4v16"/></svg>Nutrition</h3><p>Lorem ipsum dolor sit amet, consectetuer adipiscing elit. Aenean commodo ligula eget dolor. Aenean massa.</p></div>
<div class="abs pillar" style="left:478px;top:1488px"><h3><svg width="24" height="24" viewBox="0 0 24 24" fill="none" stroke="#fff" stroke-width="2"><circle cx="12" cy="12" r="9"/><path d="M5 9l14 6M9 4l6 16"/></svg>Movement</h3><p>Lorem ipsum dolor sit amet, consectetuer adipiscing elit. Aenean commodo ligula eget dolor. Aenean massa.</p></div>
<div class="abs pillar" style="left:833px;top:1488px"><h3><svg width="24" height="24" viewBox="0 0 24 24" fill="none" stroke="#fff" stroke-width="2"><path d="M4 20L20 4M8 20l-4-4M12 16l-4-4M16 12l-4-4"/></svg>Tribe</h3><p>Lorem ipsum dolor sit amet, consectetuer adipiscing elit. Aenean commodo ligula eget dolor. Aenean massa.</p></div>
<div class="abs pillar" style="left:301px;top:1681px"><h3><svg width="24" height="24" viewBox="0 0 24 24" fill="none" stroke="#fff" stroke-width="2"><circle cx="12" cy="5" r="2.5"/><path d="M4 19c3-4 13-4 16 0M8 12l4 3 4-3"/></svg>Mindfulness</h3><p>Lorem ipsum dolor sit amet, consectetuer adipiscing elit. Aenean commodo ligula eget dolor. Aenean massa.</p></div>
<div class="abs pillar" style="left:642px;top:1681px"><h3><svg width="24" height="24" viewBox="0 0 24 24" fill="none" stroke="#fff" stroke-width="2"><circle cx="12" cy="12" r="9"/><circle cx="12" cy="12" r="5"/><circle cx="12" cy="12" r="1.5" fill="#fff"/></svg>Purpose</h3><p>Lorem ipsum dolor sit amet, consectetuer adipiscing elit. Aenean commodo ligula eget dolor. Aenean massa.</p></div>

<!-- video -->
<div class="abs video-title">WATCH <span>THIS</span> VIDEO</div>
<div class="abs video-sub">You'll get all informations about Dr.Korvel</div>
<div class="abs video" role="img" aria-label="Video still of Dr. Korvel speaking on a TV studio stage before an audience"></div>
<div class="abs play"><svg width="44" height="44" viewBox="0 0 44 44"><path d="M18 14l12 8-12 8z" fill="#fff"/></svg></div>

<!-- signup -->
<div class="abs signup"></div>
<div class="abs signup-text">Sign Me Up for One on One Coaching with <span>Dr. Korvel</span></div>
<div class="abs btn-sign">sign up now</div>

<!-- testimonials -->
<div class="abs testi"></div>
<div class="abs testi-title">CLIENT TESTIMONIALS</div>
<div class="abs arrow" style="left:150px">‹</div>
<div class="abs arrow" style="left:1040px">›</div>

<div class="abs card" style="left:188px"><p>Lorem ipsum dolor sit amet, consectetuer adipiscing elit. Aenean commodo ligula eget dolor. ligula eget dolor.</p><h4>Ravi Menon</h4></div>
<div class="abs avatar" style="left:277px" role="img" aria-label="Client portrait"></div>
<div class="abs card" style="left:473px"><p>Lorem ipsum dolor sit amet, consectetuer adipiscing elit. Aenean commodo ligula eget dolor. ligula eget dolor.</p><h4>Arjun</h4></div>
<div class="abs avatar" style="left:562px" role="img" aria-label="Client portrait"></div>
<div class="abs card" style="left:758px"><p>Lorem ipsum dolor sit amet, consectetuer adipiscing elit. Aenean commodo ligula eget dolor. ligula eget dolor.</p><h4>Lakshmi</h4></div>
<div class="abs avatar" style="left:846px" role="img" aria-label="Client portrait"></div>

<!-- footer -->
<div class="abs footer" role="img" aria-label="Blue-tinted photo of Dr. Korvel behind the consultation call to action"></div>
<div class="abs foot-title">FREE CONSULTATION FIRST TIME</div>
<div class="abs foot-sub">Hurry up! only limited slots left this month.</div>
<div class="abs btn-foot">MAKE AN APPOINTMENT</div>
<div class="abs foot-call">or&nbsp; Call: (800) 555 0142</div>
<div class="abs socials">
  <div class="social" aria-label="Social link"></div>
  <div class="social" aria-label="Social link"></div>
  <div class="social" aria-label="Social link"></div>
  <div class="social" aria-label="Social link"></div>
  <div class="social" aria-label="Social link"></div>
  <div class="social" aria-label="Social link"></div>
</div>
<div class="abs copy">Copyright © 2019 korvel.com. All rights reserved.</div>

</body>
</html>
```